依頼詳細
【サイトマップ】
TOPページ
---HOME
---COMPANY (会社概要/会社沿革)
---BUSINESS (事業内容)
---RECRUIT  (採用情報)
---CONTACT  (問い合わせ)
---NEWS  (新着情報)
【サイト作成においてのポイント】
・レスポンシブデザインでお願いいたします。
・各所の素材は全てURLをお送り下さい。

【イメージ全体配置構図(いれていただきたい要素)】

ワイヤーフレームをご確認ください。
①~⑧までワイヤーフレーム内にふった番号順に詳細を記載しております。

※ワイヤーフレームはあくまでも入れたい要素を並べた一例になります。
各配置、表示位置は変えていただいても問題ございません。
------------------------

①グローバルナビ
配置は上部でお願いいたします。位置は中央を希望いたします。
------

②メインビジュアル
メインビジュアルは動画(アニメーション)挿入の仕様想定で作成して頂きたいです。
参考サイト:http://www.kelvora-sample.com/
http://updates.pimaru-breeze.jp/

1ページまるごと動画(アニメーション)仕様でも問題ございません。
参考サイト:http://www.tosquivel.com/

(こちらでは素材を用意しておりません。確認後、購入手続きをさせていただきますのでURLをお送りください)
サイズはどのデバイスでも横幅が100%になるように考えております。
縦幅はお任せしますので、素材にあわせていただけますと幸いです。
------

③新着情報
新着情報は3つ以上いれていただけますと幸いです
いれていただきたい要素は
・更新日時(年,月,日)
・更新内容のテキスト部分 20文字前後

各テキストの配置箇所、文字色、フォント、文字やボタンのサイズ、幅感等の指定はございません。
ワイヤーフレームにはいれていただきたい要素だけならべています。
------

④事業紹介箇所
入れていただきたい要素は以下になります。
・事業紹介イメージ素材
メイン動画がヘッダー部分のみに表示の場合
背景画像として、サイズは横が100%になるように考えております。
メイン動画が全体の場合
イメージ素材が浮き上がってくるようなアニメーション仕様で考えておりますので、その仕様にあったサイズ、表示方法にしていただけますと幸いです。

極力どのデバイスサイズでもバランスよく見えるような素材をご使用いただけますと幸いです。

・事業内容の名前
(Internet media、Promotion、Influencer Marketing)
・以下テキスト
(KanoMireaはインターネットを軸とした事業を展開しております。)
・下層ページへのリンクボタン

------

⑤入れていただきたい要素は以下になります。
・背景素材
メイン動画がヘッダー部分のみに表示の場合
メイン動画が全体の場合

・遷移先の中に含まれる内容の紹介
(Staff Interview、One Day、Blog)
・以下テキスト
(KanoMireaの福利厚生や、メンバーの1日の勤務スケジュールを公開)
・下層ページへのリンクボタン

------

⑥入れていただきたい要素は以下になります。
・背景素材
メイン動画がヘッダー部分のみに表示の場合
メイン動画が全体の場合

・遷移先の中に含まれる内容の紹介
(overview/ history、Greeting)
・以下テキスト
(会社概要・沿革・代表挨拶)
・下層ページへのリンクボタン

------

⑦フッター
サイト案内
------

⑧会社情報、ロゴ

以上になります。

ご不明点等がございましたらお気軽にお問い合わせ下さい。
何卒よろしくお願い申し上げます。
ページ数
1ページ
希望イメージ
• +5 0 +5
• シンプル
複雑
• 単色
カラフル
• 暗い
明るい
• 日常
高級
• 遊び心
厳粛
• 未来的
伝統的
• 女性的
男性的
希望する色
青系、水色系、グレー系、紫系
納品ファイル
• フォトショップ形式 (.psd)
補足説明
SD又は、FireworksPNGデータ
動画に関しましてはデータ添付またはURLをお送りいただけますと幸いです。
依頼公開後の追記内容
もう少し様々な作品を拝見させていただきたく、延長させていただきました。
引き続き、何卒よろしくお願いいたします。
■ 選んだ理由

全体の雰囲気が1番理想とするものに近く、構図も綺麗なバランスで組み立てられていました。
コーポレートサイトとしてシンプルかつおしゃれ見やすいものに仕上がると思い、rusofu様の作品を選ばせていただきました。

■ 提案者全員のお礼・コメント

各ランサー様
この度は弊社へのコンペへご参加いただき、誠にありがとうございました。
どの作品も大変素晴らしく、当選させていただきたいアイディア、デザインがたくさんありました。
また機会がございましたら、作品をご投稿下さいますと幸いに存じます。
誠にありがとうございました。

```html
<!DOCTYPE html>
<html lang="ja">
<head>
<meta charset="utf-8">
<title>KanoMirea | Total Web Solutions</title>
<link href="https://fonts.googleapis.com/css2?family=Noto+Sans+JP:wght@400;500;700&family=Oswald:wght@400;500;600&display=swap" rel="stylesheet">
<style>
:root{
  --blue:#3f86b6;
  --blue-dark:#2f6f9c;
  --footer:#4f88b0;
  --footer-deep:#3d7aa4;
  --teal:#4d9aa6;
  --mint:#d9f6ea;
  --sky:#d2e7f3;
  --ink:#3a4a58;
  --grey:#8a95a0;
  --white:#ffffff;
}
*{box-sizing:border-box;margin:0;padding:0}
html,body{width:1200px;height:3184px;overflow:hidden}
body{font-family:"Noto Sans JP",sans-serif;color:var(--ink);background:#fff;position:relative}
.global-nav{position:absolute;top:0;left:50%;transform:translateX(-50%);z-index:5;background:var(--blue-dark);display:flex;gap:34px;padding:6px 30px;font-family:"Oswald",sans-serif;font-size:11px;color:#fff;letter-spacing:.08em}
.hero{position:relative;height:740px;overflow:hidden}
.hero-visual{position:absolute;inset:0;background:radial-gradient(ellipse at 50% 40%,#ffffff 0%,#e9edf0 45%,#c6ced5 100%)}
.brand{display:flex;align-items:center;gap:10px;font-family:"Noto Sans JP",sans-serif;font-weight:700;color:var(--blue);white-space:nowrap}
.brand-dot{flex:0 0 auto;width:44px;height:44px;border-radius:50%;background:var(--blue)}
.hero .brand{position:absolute;top:110px;left:50%;transform:translateX(-50%);font-size:34px}
.hero-copy{position:absolute;top:590px;width:100%;text-align:center}
.hero-title{font-family:"Oswald",sans-serif;font-weight:600;font-size:52px;letter-spacing:.06em;color:var(--blue)}
.hero-sub{font-weight:700;font-size:22px;color:var(--blue-dark);margin-top:2px}
.news{height:140px;background:#f1f3f4;display:flex;align-items:center;padding:0 180px}
.news-head{width:210px;border-left:4px solid var(--blue);padding-left:14px}
.news-head h2{font-family:"Oswald",sans-serif;font-size:22px;letter-spacing:.15em;color:var(--blue)}
.news-head p{font-size:11px;color:var(--grey)}
.news-list{list-style:none;flex:1;font-size:12px;color:var(--grey);line-height:2}
.news-list time{margin-right:18px}
.btn{display:inline-block;width:130px;height:34px;line-height:32px;text-align:center;border:1px solid var(--blue);background:#fff;font-family:"Oswald",sans-serif;font-size:12px;color:var(--blue);letter-spacing:.1em}
.section{position:relative;text-align:center}
.section-title{font-family:"Oswald",sans-serif;font-weight:600;font-size:44px;letter-spacing:.12em;color:var(--blue)}
.section-lead{font-size:14px;color:var(--ink);margin-top:4px}
.business{height:620px;background:var(--mint);padding-top:60px}
.card-row{display:flex;gap:10px;margin:40px auto 0;width:1060px}
.card{position:relative;flex:1;height:260px}
.photo{width:100%;height:100%}
.card-label{position:absolute;left:50%;transform:translateX(-50%);bottom:-40px;width:100px;height:90px;background:var(--teal);color:#fff;font-family:"Oswald",sans-serif;font-size:16px;display:flex;align-items:center;justify-content:center;line-height:1.2}
.business .btn{margin-top:70px}
.recruit{height:600px;padding-top:50px}
.section-bg{position:absolute;inset:0;z-index:0}
.section > *:not(.section-bg){position:relative;z-index:1}
.frame{margin:36px auto 0;width:1060px;border:14px solid var(--blue);display:flex;gap:10px;height:260px;background:var(--blue)}
.frame .card{height:232px}
.circle-label{position:absolute;left:50%;bottom:-70px;transform:translateX(-50%);width:110px;height:110px;border-radius:50%;background:var(--teal);border:5px solid #fff;color:#fff;font-family:"Oswald",sans-serif;font-size:16px;display:flex;align-items:center;justify-content:center;line-height:1.2}
.recruit .btn{margin-top:90px}
.company{height:560px;background:var(--sky);padding-top:60px}
.tab{position:absolute;top:-16px;width:140px;height:40px;line-height:40px;background:var(--teal);color:#fff;font-family:"Oswald",sans-serif;font-size:16px}
.card:nth-child(1) .tab{left:20px}
.card:nth-child(2) .tab{left:50%;transform:translateX(-50%)}
.card:nth-child(3) .tab{right:20px}
.company .btn{margin-top:50px}
.contact{position:relative;height:260px}
.contact-bg{position:absolute;inset:0;background:linear-gradient(#d3d7d9,#a3abb0 60%,#7d878e)}
.contact-panel{position:absolute;left:50%;top:40px;transform:translateX(-50%);width:300px;height:180px;background:rgba(46,58,68,.92);color:#fff;text-align:center;padding-top:20px}
.contact-panel h2{font-family:"Oswald",sans-serif;font-size:28px;letter-spacing:.12em;line-height:1.2}
.contact-panel .brand{color:#fff;font-size:14px;justify-content:center;margin:6px 0 10px;gap:8px}
.contact-panel .brand-dot{width:14px;height:14px;background:#fff}
.contact-panel p{font-size:11px;line-height:1.6}
.contact-panel span{display:inline-block;margin-top:8px;padding:3px 14px;background:var(--teal);font-size:11px}
.site-map{height:140px;background:var(--footer);display:flex;justify-content:center;gap:56px;padding-top:26px;color:#fff;font-size:11px}
.site-map h3{font-family:"Oswald",sans-serif;font-weight:500;font-size:13px;letter-spacing:.06em;border-bottom:1px solid rgba(255,255,255,.6);padding-bottom:3px;margin-bottom:4px;min-width:110px}
.site-map li{list-style:none;line-height:1.6;opacity:.9}
.site-info{height:124px;background:var(--footer-deep);display:flex;align-items:center;justify-content:center;gap:50px;color:#fff;font-size:11px;line-height:1.6;position:relative}
.site-info .brand{color:#fff;font-size:26px}
.site-info .brand-dot{width:32px;height:32px;background:#fff}
.copyright{position:absolute;bottom:8px;width:100%;text-align:center;font-size:9px;opacity:.8}
</style>
</head>
<body>
<nav class="global-nav"><span>HOME</span><span>BUSINESS</span><span>RECRUIT</span><span>COMPANY</span><span>CONTACT</span><span>NEWS</span></nav>

<header class="hero">
  <div class="hero-visual" role="img" aria-label="Main visual video: soft white spheres floating in a pale grey space"></div>
  <div class="brand"><span class="brand-dot"></span>Kano Mirea</div>
  <div class="hero-copy">
    <h1 class="hero-title">TOTAL WEB SOLUTIONS</h1>
    <p class="hero-sub">先進のデジタルマーケティングを全方位でご提供</p>
  </div>
</header>

<section class="news">
  <div class="news-head"><h2>NEWS</h2><p>新着情報</p></div>
  <ul class="news-list">
    <li><time>2019年11月10日</time>新サービスの提供を開始しました（詳細ページ）</li>
    <li><time>2019年11月03日</time>採用情報ページを更新しました（募集要項）</li>
    <li><time>2019年10月28日</time>年末年始の営業日をお知らせします（詳細）</li>
  </ul>
  <a class="btn">more</a>
</section>

<section class="section business">
  <h2 class="section-title">BUSINESS</h2>
  <p class="section-lead">KanoMireaはインターネットを軸とした事業を展開しております。</p>
  <div class="card-row">
    <div class="card"><div class="photo" role="img" aria-label="Laptop on a desk showing a web page" style="background:linear-gradient(135deg,#e9e4dc,#b9b2a8)"></div><div class="card-label">Internet<br>Media</div></div>
    <div class="card"><div class="photo" role="img" aria-label="Hands holding a smartphone at a table" style="background:linear-gradient(135deg,#d9d2c8,#9c8f82)"></div><div class="card-label">Promotion</div></div>
    <div class="card"><div class="photo" role="img" aria-label="Tablet with growth charts on a desk" style="background:linear-gradient(135deg,#f0f0ee,#c3c6c8)"></div><div class="card-label">Influencer<br>Marketing</div></div>
  </div>
  <a class="btn">more</a>
</section>

<section class="section recruit">
  <div class="section-bg" role="img" aria-label="Faded office interior in the background" style="background:linear-gradient(#eef1f2,#d9dee1)"></div>
  <h2 class="section-title">RECRUIT</h2>
  <p class="section-lead">KanoMireaの福利厚生や、メンバーの1日の勤務スケジュールを公開</p>
  <div class="frame">
    <div class="card"><div class="photo" role="img" aria-label="Staff member at work in a bright office" style="background:linear-gradient(135deg,#f3efe9,#c9c2b8)"></div><div class="circle-label">Staff<br>Interview</div></div>
    <div class="card"><div class="photo" role="img" aria-label="Team hands together over a desk" style="background:linear-gradient(135deg,#dfe3e6,#8e9aa3)"></div><div class="circle-label">One Day</div></div>
    <div class="card"><div class="photo" role="img" aria-label="Person writing at a laptop" style="background:linear-gradient(135deg,#eef0f1,#b4bcc2)"></div><div class="circle-label">Blog</div></div>
  </div>
  <a class="btn">more</a>
</section>

<section class="section company">
  <h2 class="section-title">COMPANY</h2>
  <p class="section-lead">KanoMireaの会社概要・代表挨拶・沿革です。</p>
  <div class="card-row">
    <div class="card"><div class="photo" role="img" aria-label="Reception wall in warm light" style="background:linear-gradient(135deg,#7a5a3c,#3c2e24)"></div><div class="tab">Overview</div></div>
    <div class="card"><div class="photo" role="img" aria-label="Representative standing in a modern office" style="background:linear-gradient(135deg,#b9bcbe,#5d6266)"></div><div class="tab">Greeting</div></div>
    <div class="card"><div class="photo" role="img" aria-label="Office corridor with glass walls" style="background:linear-gradient(135deg,#8b7560,#3f3832)"></div><div class="tab">History</div></div>
  </div>
  <a class="btn">more</a>
</section>

<section class="contact">
  <div class="contact-bg" role="img" aria-label="Meeting room with a laptop on a long table"></div>
  <div class="contact-panel">
    <h2>CONTACT</h2>
    <div class="brand"><span class="brand-dot"></span>Kano Mirea</div>
    <p>お気軽にお問い合わせください<br>担当者よりご連絡いたします</p>
    <span>メールでのお問い合わせ</span>
  </div>
</section>

<footer>
  <div class="site-map">
    <div><h3>HOME</h3></div>
    <div><h3>BUSINESS 事業内容</h3><ul><li>Internet Media</li><li>Promotion</li><li>Influencer Marketing</li></ul></div>
    <div><h3>RECRUIT 採用情報</h3><ul><li>Staff Interview</li><li>One Day</li><li>Blog</li></ul></div>
    <div><h3>COMPANY 会社概要</h3><ul><li>Overview</li><li>Greeting</li><li>History</li></ul></div>
    <div><h3>CONTACT お問い合わせ</h3></div>
    <div><h3>NEWS 新着情報</h3></div>
  </div>
  <div class="site-info">
    <div class="brand"><span class="brand-dot"></span>Kano Mirea</div>
    <div>株式会社 KanoMirea<br>〒100-0000 東京都サンプル区みなと1-2-3<br>TEL 00-0000-0000</div>
    <p class="copyright">Copyright © KanoMirea Inc. All Rights Reserved.</p>
  </div>
</footer>
</body>
</html>
```